Rinzo Pizza & Pasta Takeaway Flyer

Our takeaway shop needs a well designed flyer for print and letter box distribution. Design to have a clear list of menu, Specials, contact details. If menu doesn't fit into A4, we won't mind going upto extended A4. I have attached draft copy of our menu and list of item in excel. Please add 5mm Bleed to the flyer.
Flyer will get printed on 115gsm Gloss stock.

```html
<!DOCTYPE html>
<html lang="en">
<head>
<meta charset="utf-8">
<title>Rinzo Pizza &amp; Pasta – Takeaway Menu</title>
<link href="https://fonts.googleapis.com/css2?family=Oswald:wght@500;700&family=Roboto+Condensed:ital,wght@0,400;0,500;1,400&display=swap" rel="stylesheet">
<style>
:root{
  --bg:#1a5f8c;
  --paper:#ffffff;
  --paper-shade:#efefef;
  --maroon:#5a0f12;
  --yellow:#ffd21a;
  --ink:#3a1414;
  --ink-soft:#5a2a2a;
  --ghost:#e6e6e6;
}
*{margin:0;padding:0;box-sizing:border-box}
html,body{width:1200px;height:1200px;overflow:hidden;background:var(--bg)}
.menu{position:absolute;left:12px;top:290px;width:1337px;height:703px;transform:scale(.88);transform-origin:0 0;
  font-family:"Roboto Condensed",sans-serif;color:var(--ink);display:flex}
.panel{position:relative;height:100%;background:linear-gradient(90deg,var(--paper) 70%,var(--paper-shade));overflow:hidden}
.p1{width:330px}.p2{width:333px}.p3{width:337px}.p4{width:337px}
.tag{position:absolute;height:37px;background:var(--maroon);color:var(--yellow);font-family:"Oswald",sans-serif;font-weight:700;
  font-size:20px;line-height:37px;padding-left:28px;clip-path:polygon(0 0,100% 0,88% 50%,100% 100%,0 100%)}
.box{position:absolute;background:var(--maroon);color:var(--yellow);font-family:"Oswald",sans-serif;font-weight:700;
  text-align:center;border:2px solid var(--paper);outline:1px solid var(--maroon);line-height:1}
.box.title{font-size:20px;display:flex;align-items:center;justify-content:center}
.box.price{font-size:15px;padding-top:2px}
.box.price b{display:block;font-size:15px;font-weight:700}
.list{position:absolute;list-style:none}
.item{display:flex;align-items:baseline;font-size:14.5px;line-height:16px}
.item .lead{flex:1;border-bottom:1px dotted var(--ink-soft);margin:0 4px 4px 1px}
.item .cost{white-space:nowrap}
.desc{font-size:9px;font-style:italic;line-height:10px;color:var(--ink-soft)}
.list li{margin-bottom:6px}
.names li{font-size:14.5px;line-height:16px}
.names li{margin-bottom:5px}
.note{position:absolute;font-size:14px;line-height:18px}
.badge{position:absolute;left:160px;top:444px;width:46px;height:46px;border-radius:50%;background:var(--maroon);color:var(--yellow);
  font-family:"Oswald",sans-serif;font-weight:700;font-size:16px;line-height:15px;text-align:center;padding-top:6px;border:2px solid var(--paper);outline:1px solid var(--maroon)}
.ghost{position:absolute;background:var(--ghost);opacity:.7}
</style>
</head>
<body>
<main class="menu" aria-label="Rinzo Pizza &amp; Pasta takeaway menu">

<section class="panel p1">
  <div class="ghost" role="img" aria-label="Faint bread slice decoration" style="left:200px;top:40px;width:110px;height:70px;border-radius:20px"></div>
  <div class="ghost" role="img" aria-label="Faint fries carton decoration" style="left:140px;top:270px;width:80px;height:110px;border-radius:10px"></div>
  <div class="ghost" role="img" aria-label="Faint garlic sub roll decoration" style="left:230px;top:470px;width:90px;height:110px;border-radius:45px"></div>
  <div class="ghost" role="img" aria-label="Faint roast chicken decoration" style="left:250px;top:620px;width:60px;height:60px;border-radius:50%"></div>

  <div class="tag" style="left:0;top:22px;width:132px">STARTER</div>
  <ul class="list" style="left:30px;top:73px;width:270px">
    <li><div class="item"><span>Garlic Bread</span><span class="lead"></span><span class="cost">$ 3.95</span></div></li>
    <li><div class="item"><span>Cheesy Garlic Bread</span><span class="lead"></span><span class="cost">$ 5.5</span></div></li>
    <li><div class="item"><span>Sweet Chilli Cheese Pizza</span><span class="lead"></span><span class="cost">$ 7.95</span></div><div class="desc">Sweet Chilli Sauce Base topped with Cheese &amp; Herbs</div></li>
    <li><div class="item"><span>Chips(Lge+$2)</span><span class="lead"></span><span class="cost">$ 4.95</span></div><div class="desc">With Tomato Sauce</div></li>
    <li><div class="item"><span>Chips &amp; Gravy</span><span class="lead"></span><span class="cost">$ 6.95</span></div></li>
    <li><div class="item"><span>Beer Battered Chips</span><span class="lead"></span><span class="cost">$ 6.95</span></div></li>
    <li><div class="item"><span>Curly Fries (Lge+$2.5)</span><span class="lead"></span><span class="cost">$ 5.95</span></div><div class="desc">With Ranch Dip</div></li>
    <li><div class="item"><span>Sweet Potato Chips</span><span class="lead"></span><span class="cost">$ 6.95</span></div><div class="desc">With Garlic Aioli Sauce</div></li>
    <li><div class="item"><span>Onion Rings</span><span class="lead"></span><span class="cost">$ 6.5</span></div><div class="desc">With Ranch Dip</div></li>
    <li><div class="item"><span>Chicken Nuggets (8Pcs)</span><span class="lead"></span><span class="cost">$ 6.5</span></div><div class="desc">With Tomato Sauce</div></li>
    <li><div class="item"><span>Pepper Squid</span><span class="lead"></span><span class="cost">$ 0.00</span></div></li>
    <li><div class="item"><span>Chicken Chilli</span><span class="lead"></span><span class="cost">$ 7.95</span></div><div class="desc">With Lemon Wedge</div></li>
  </ul>

  <div class="tag" style="left:0;top:448px;width:156px">GARLIC SUB</div>
  <div class="badge">$<br>9.95</div>
  <ul class="list names" style="left:30px;top:499px;width:260px">
    <li>Pulled Beef<div class="desc">Cheese, PulledBeef, Salami, Onion, Mushroom with BBQSauce</div></li>
    <li style="margin-top:8px">Chicken<div class="desc">Cheese, SeasonedChicken, Tomato, Onion, Fetta with<br>Sweet Chilli Sauce</div></li>
    <li style="margin-top:8px">Veg<div class="desc">Cheese, Tomato, Onion, Mushroom, Capsicum, Pineapple with<br>Tomato Sauce</div></li>
    <li style="margin-top:8px">Meat<div class="desc">Cheese, Ham, Pepperoni, Salami, Sausage with BBQ Sauce</div></li>
    <li style="margin-top:8px">Bacon &amp; Chicken<div class="desc">Cheese, SeasonedChicken, Bacon, Mushroom with PeriPeri Sauce</div></li>
  </ul>
</section>

<section class="panel p2">
  <div class="ghost" role="img" aria-label="Faint whole pizza decoration" style="left:165px;top:92px;width:140px;height:140px;border-radius:50%"></div>
  <div class="ghost" role="img" aria-label="Faint pizza slice decoration" style="left:180px;top:370px;width:140px;height:50px;border-radius:25px"></div>

  <div class="tag" style="left:0;top:22px;width:104px">PIZZA</div>
  <div class="box title" style="left:33px;top:61px;width:50px;height:35px">LITE</div>
  <div class="box price" style="left:109px;top:61px;width:50px;height:35px">Small<b>$ 9</b></div>
  <div class="box price" style="left:182px;top:61px;width:49px;height:35px">Large<b>$ 13</b></div>
  <div class="box price" style="left:254px;top:61px;width:51px;height:35px">Family<b>$ 20</b></div>
  <ul class="list names" style="left:34px;top:100px;width:260px">
    <li>Hawaiian<div class="desc">Cheese, Ham &amp; Pineapple</div></li>
    <li>Margherita<div class="desc">Cheese, Tomatoes, Basil&amp;Oregano</div></li>
    <li>Mozzy<div class="desc">Cheese, Basil &amp; Oregano</div></li>
    <li>New Yorker<div class="desc">Pepperoni, Basil&amp;Oregano</div></li>
    <li>Veggie<div class="desc">Onion, Tomato, Mushroom, Capsicum, Olives, Pineapple,<br>Basil &amp; Oregano</div></li>
  </ul>

  <div class="box title" style="left:33px;top:268px;width:77px;height:36px">CLASSIC</div>
  <div class="box price" style="left:125px;top:268px;width:50px;height:36px">Small<b>$ 11</b></div>
  <div class="box price" style="left:190px;top:268px;width:49px;height:36px">Large<b>$ 15</b></div>
  <div class="box price" style="left:254px;top:268px;width:51px;height:36px">Family<b>$ 22</b></div>
  <ul class="list names" style="left:34px;top:308px;width:270px">
    <li>Supreme<div class="desc">Cheese, Pepperoni, Ham, Beef, Onion, Olives, Capsicum,<br>Pineapple &amp; Mushroom</div></li>
    <li>Meat Lovers<div class="desc">Cheese, Pepperoni, Salami, Ham, Bacon, Sausage &amp; BBQ Sauce</div></li>
    <li>Ozzy<div class="desc">Cheese, Sausage, Bacon, Onion &amp; Egg</div></li>
    <li>BBQ Chicken<div class="desc">Cheese, Chicken, Bacon, Mushroom &amp; BBQ Sauce</div></li>
    <li>Tropical Chicken<div class="desc">Cheese, Chicken, Ham, Pineapple</div></li>
    <li>Outback<div class="desc">Cheese, Ham, Salami, Bacon, Mushroom &amp; Onion</div></li>
    <li>Spicy Pizza<div class="desc">Cheese, Pepperoni, Onion, Jalapenos &amp; Chili Flakes</div></li>
    <li>Mexican<div class="desc">Cheese, Beef, Pepperoni, Onion, Roasted Capsicum, Jalapenos,<br>Chilli &amp; Sourcream</div></li>
    <li>Capricciosa<div class="desc">Cheese, Ham, Salami, Mushroom, Tomato &amp; Olives</div></li>
    <li>Veg Supreme<div class="desc">Cheese, Tomato, Onion, Mushroon, Roasted Capsicum, Pineapple,<br>Fetta, Jalapenos &amp; Chilli</div></li>
    <li>Four Cheese<div class="desc">Cheese, Fetta, Bocconcini, Parmesan &amp; Basil</div></li>
  </ul>
</section>

<section class="panel p3">
  <div class="box title" style="left:33px;top:21px;width:84px;height:37px">PREMIUM</div>
  <div class="box price" style="left:126px;top:21px;width:50px;height:37px">Small<b>$ 13</b></div>
  <div class="box price" style="left:190px;top:21px;width:50px;height:37px">Large<b>$ 19</b></div>
  <div class="box price" style="left:256px;top:21px;width:52px;height:37px">Family<b>$ 25</b></div>
  <ul class="list names" style="left:37px;top:63px;width:280px">
    <li>Garden Gourmet<div class="desc">Cheese, Semi-dried tomato, Mushrooms, Onion, Roasted Capsicum,<br>Olives, Cherry Tomato, Spinach, Bocconcini &amp; Basil</div></li>
    <li>Paneer Tikka<div class="desc">Cheese, Marinated Paneer, Onion, Tomato, Capsicum, Olives &amp; Corinander</div></li>
    <li>Pesto Chicken<div class="desc">Cheese, Chicken, Sun-Dried Tomato, Onion, Fetta &amp; Parsley</div></li>
    <li>Butter Chicken<div class="desc">Cheese, Marinated Chicken, Onion, Capsicum, Corinader,<br>Cashew &amp; Lemon Wedge</div></li>
    <li>Meat &amp; Chicken<div class="desc">Pulled Beef, Pepperoni, Chicken, Salami, Roasted Capsicum, Mushroom,<br>Onion &amp; BBQ Sauce</div></li>
    <li>Mediterranean<div class="desc">Pepperoni, Roasted Capsicum, Mushroom, Sausage, Olives,<br>Fetta &amp; Bocconcini</div></li>
  </ul>

  <div class="box title" style="left:33px;top:310px;width:84px;height:37px">SEAFOOD</div>
  <div class="box price" style="left:128px;top:310px;width:50px;height:37px">Small<b>$ 14</b></div>
  <div class="box price" style="left:192px;top:310px;width:50px;height:37px">Large<b>$ 21</b></div>
  <div class="box price" style="left:257px;top:310px;width:52px;height:37px">Family<b>$ 28</b></div>
  <ul class="list names" style="left:37px;top:351px;width:280px">
    <li>The Pacific<div class="desc">Seafood Mix, Mushrooms, Roasted Capsicum &amp; Garlic Oil<br>(AnchoviesSuggested)</div></li>
    <li>Reef n Turf<div class="desc">Prawn, Pulled Beef, Onion, Mushroom, Capsicum, Olives &amp; Garlic Sauce</div></li>
    <li>Reef n Turf<div class="desc">Prawns, Cheery Tomato, Spinach, Bocconcini &amp; Garlic Sauce</div></li>
  </ul>
  <div class="note" style="left:37px;top:455px;width:280px">
    ** Thin Base Available **<br>
    <span style="display:block;margin-top:3px">** GF base available only in large size. Extra $3 **</span>
    <span style="display:block;margin-top:4px;padding-left:18px;text-indent:-18px">** Each Extra Topping - Small $1, Large $2, Family $3 **</span>
  </div>

  <div class="tag" style="left:4px;top:545px;width:160px">GARLIC SUB</div>
  <ul class="list" style="left:37px;top:594px;width:270px">
    <li><div class="item"><span>Classic Calzone</span><span class="lead"></span><span class="cost">$ 16</span></div><div class="desc">Folded Pizza, Rolled &amp; Cooked, Sealing in all Flaours<br>from Classic Pizza range.</div></li>
    <li style="margin-top:8px"><div class="item"><span>Premium Calzone</span><span class="lead"></span><span class="cost">$ 18</span></div><div class="desc">Folded Pizza, Rolled &amp; Cooked, Sealing in all Flaours<br>from Premium Pizza range.</div></li>
  </ul>
</section>

<section class="panel p4">
  <div class="tag" style="left:2px;top:22px;width:110px">PASTA</div>
  <ul class="list" style="left:36px;top:63px;width:268px">
    <li><div class="item"><span>Napoletana</span><span class="lead"></span><span class="cost">$ 14</span></div><div class="desc">Tomatoes, Onions, and Special Italian Herbs in Red Pasta sauce</div></li>
    <li><div class="item"><span>Vegetaria</span><span class="lead"></span><span class="cost">$ 16</span></div><div class="desc">Mushroom, Tomatoes, Onions,Capsicum and Special Italian Herbs<br>in Red Pasta sauce</div></li>
    <li><div class="item"><span>Bolognese</span><span class="lead"></span><span class="cost">$ 16</span></div><div class="desc">Traditional Beef, Onions and Special Italian Herbs in Red Pasta sauce</div></li>
    <li><div class="item"><span>Carbonara</span><span class="lead"></span><span class="cost">$ 16</span></div><div class="desc">Bacon, Eggs &amp; Mushrooms in a Creamy White Sauce</div></li>
    <li><div class="item"><span>Alla Panna</span><span class="lead"></span><span class="cost">$ 16</span></div><div class="desc">Ham &amp; Mushrooms in a Creamy White Sauce</div></li>
    <li><div class="item"><span>Chicken Carbonara</span><span class="lead"></span><span class="cost">$ 16</span></div><div class="desc">Chicken, Eggs, Mushrooms &amp; Onions in a Creamy White Sauce</div></li>
    <li><div class="item"><span>Chicken</span><span class="lead"></span><span class="cost">$ 16</span></div><div class="desc">Chicken, Tomato, Pesto in a Creamy White Sauce</div></li>
    <li><div class="item"><span>Greek Chicken</span><span class="lead"></span><span class="cost">$ 16</span></div><div class="desc">Chicken, Tomato, Fetta, Olives in a Red Pasta Sauce</div></li>
    <li><div class="item"><span>Garlic Prawn</span><span class="lead"></span><span class="cost">$ 18</span></div><div class="desc">Prawn, Garlic, Onion, Lemon in a Creamy White Sauce</div></li>
    <li><div class="item"><span>Puttanesca</span><span class="lead"></span><span class="cost">$ 18</span></div><div class="desc">Anchovies, Olives, Capers in a Red Pasta Sauce</div></li>
    <li><div class="item"><span>Marinara</span><span class="lead"></span><span class="cost">$ 18</span></div><div class="desc">Seafood mix in a Red Pasta Sauce</div></li>
  </ul>

  <div class="tag" style="left:2px;top:422px;width:296px;font-size:18px;clip-path:polygon(0 0,100% 0,93% 50%,100% 100%,0 100%)">MAIN <span style="font-size:12px">(Served with Chips &amp; Garden Salad)</span></div>
  <ul class="list" style="left:36px;top:462px;width:268px">
    <li style="margin-bottom:3px"><div class="item"><span>Chicken Schnitzel with Gravy</span><span class="lead"></span><span class="cost">$ 16</span></div></li>
    <li style="margin-bottom:3px"><div class="item"><span>Veal Schnitzel with Gravy</span><span class="lead"></span><span class="cost">$ 16</span></div></li>
    <li style="margin-bottom:3px"><div class="item"><span>Chicken Parmigiana</span><span class="lead"></span><span class="cost">$ 17</span></div></li>
    <li><div class="item"><span>Three Cheese Parmigiana</span><span class="lead"></span><span class="cost">$ 17</span></div><div class="desc">Topped with Parmesan, Mozzarella, Bocconcini &amp; Herbs</div></li>
    <li><div class="item"><span>Hawiian Parmigiana</span><span class="lead"></span><span class="cost">$ 17</span></div><div class="desc">Topped with Cheese, Ham, Pineapple &amp; Herbs</div></li>
    <li><div class="item"><span>Mexican Parmigiana</span><span class="lead"></span><span class="cost">$ 17</span></div><div class="desc">Topped with Cheese, Roasted Capsicum, Jalapenos &amp; Herbs</div></li>
    <li><div class="item"><span>Marinara Parmigiana</span><span class="lead"></span><span class="cost">$ 19</span></div><div class="desc">Topped with Cheese, Seafood mix &amp; Herbs</div></li>
    <li><div class="item"><span>Creamy Garlic Prawn</span><span class="lead"></span><span class="cost">$ 19</span></div><div class="desc">Tiger Prawn, Garlic, White Wine, Spices &amp; Herbs Pan fried with<br>Creamy sauce</div></li>
  </ul>
</section>

</main>
</body>
</html>
```